Harborline Stay Collective Business Card Design

Design a business card for Harborline Stay Collective. Look at the website for colors and reference. Card should have logo, name, title, office number, mobile number, email, URL and a tagline like, "Luxury Hotel & Resort Email Marketing" (This might change).

https://www.harborlinestaycollective.net

The rest I will leave up to your imagination.

Contact Information for Business Card

Logo, name, title, office number, mobile number, email, URL and a tagline like, "Luxury Hotel & Resort Email Marketing" (This might change).

```html
<!DOCTYPE html>
<html lang="en">
<head>
<meta charset="UTF-8">
<title>Harborline Stay Collective — Business Card</title>
<link rel="stylesheet" href="https://fonts.googleapis.com/css2?family=Montserrat:wght@400;500;700;800&display=swap">
<style>
  :root {
    --canvas: #1f1f21;
    --card: #262629;
    --orange: #f47320;
    --white: #ffffff;
    --text-soft: #e6e6e6;
  }
  * { margin: 0; padding: 0; box-sizing: border-box; }
  html, body { width: 1200px; height: 900px; overflow: hidden; }
  body {
    background: var(--canvas);
    font-family: "Montserrat", Arial, sans-serif;
    position: relative;
  }
  .card {
    position: absolute;
    width: 600px;
    height: 343px;
    background: var(--card);
    border-radius: 14px;
    overflow: hidden;
    box-shadow: 0 14px 40px rgba(0,0,0,0.45);
  }
  .card-front { left: 300px; top: 70px; }
  .card-back { left: 300px; top: 487px; }

  .brand-name {
    color: var(--white);
    font-weight: 800;
    text-transform: uppercase;
    letter-spacing: 1px;
    display: flex;
    align-items: center;
    gap: 12px;
  }
  .brand-mark {
    width: 14px; height: 14px;
    background: var(--orange);
    flex: none;
  }
  .card-front .brand-name {
    position: absolute;
    left: 0; right: 0; top: 150px;
    justify-content: center;
    font-size: 30px;
  }
  .card-back .brand-name {
    position: absolute;
    left: 30px; top: 160px;
    width: 220px;
    font-size: 15px;
    line-height: 1.25;
  }

  .divider {
    position: absolute;
    left: 270px; top: 70px;
    width: 2px; height: 175px;
    background: var(--orange);
  }
  .contact {
    position: absolute;
    left: 292px; top: 60px;
    color: var(--text-soft);
  }
  .person-name {
    color: var(--orange);
    font-weight: 700;
    font-size: 21px;
  }
  .person-title {
    font-size: 12px;
    margin: 2px 0 12px 0;
  }
  .address {
    font-size: 11.5px;
    line-height: 1.45;
    margin-bottom: 10px;
  }
  .contact-list { list-style: none; }
  .contact-list li {
    display: flex;
    align-items: center;
    gap: 9px;
    font-size: 11.5px;
    line-height: 1.75;
  }
  .contact-list svg { width: 12px; height: 12px; flex: none; }

  .band-orange {
    position: absolute;
    left: 0; bottom: 24px;
    width: 340px; height: 36px;
    background: var(--orange);
    clip-path: polygon(0 0, 100% 0, 96% 100%, 0 100%);
  }
  .tagline-strip {
    position: absolute;
    right: 0; bottom: 60px;
    width: 258px; height: 40px;
    background: var(--white);
    clip-path: polygon(4% 0, 100% 0, 100% 100%, 0 100%);
    display: flex;
    align-items: center;
    justify-content: center;
    color: var(--orange);
    font-weight: 700;
    font-size: 12px;
  }
</style>
</head>
<body>

  <section class="card card-front" aria-label="Card front">
    <div class="brand-name"><span class="brand-mark"></span>Harborline Stay Collective</div>
  </section>

  <section class="card card-back" aria-label="Card back">
    <div class="brand-name"><span class="brand-mark"></span>Harborline Stay Collective</div>

    <div class="divider"></div>

    <div class="contact">
      <p class="person-name">Rowan Castell</p>
      <p class="person-title">Owner</p>
      <p class="address">410 Pier Road, Suite 208<br>Portland, ME 04101</p>
      <ul class="contact-list">
        <li>
          <svg viewBox="0 0 24 24" fill="var(--orange)"><path d="M6.6 10.8a15.1 15.1 0 0 0 6.6 6.6l2.2-2.2a1 1 0 0 1 1-.25 11.4 11.4 0 0 0 3.6.57 1 1 0 0 1 1 1V20a1 1 0 0 1-1 1A17 17 0 0 1 3 4a1 1 0 0 1 1-1h3.5a1 1 0 0 1 1 1c0 1.25.2 2.45.57 3.6a1 1 0 0 1-.25 1z"/></svg>
          555.014.2288 x 112
        </li>
        <li>
          <svg viewBox="0 0 24 24" fill="none" stroke="var(--orange)" stroke-width="2.4"><rect x="6" y="2" width="12" height="20" rx="2"/><line x1="11" y1="18" x2="13" y2="18"/></svg>
          555.019.4471
        </li>
        <li>
          <svg viewBox="0 0 24 24" fill="var(--orange)"><path d="M2 5h20v14H2z"/><path d="M2 5l10 8 10-8" fill="none" stroke="var(--card)" stroke-width="2"/></svg>
          info@harborlinestaycollective.net
        </li>
        <li>
          <svg viewBox="0 0 24 24" fill="none" stroke="var(--orange)" stroke-width="2.2"><circle cx="12" cy="12" r="9.5"/><ellipse cx="12" cy="12" rx="4" ry="9.5"/><line x1="2.5" y1="12" x2="21.5" y2="12"/></svg>
          www.harborlinestaycollective.net
        </li>
      </ul>
    </div>

    <div class="tagline-strip">Luxury Hotel &amp; Resort Email Marketing</div>
    <div class="band-orange"></div>
  </section>

</body>
</html>
```